Web template for real estate developing company
KORVALD
Real Estate
www.morvinkorvald.dk
Developing real estate company in Denmark.
Consulting Competence
Handling of a project:
Analysis of local conditions and market analysis
Functional and usability concept
Analysis of profitability
Financing and utilization strategies
Economic and Technical project control
Like: Start up movement on the KORVALD logo like a dynamic building assamply on a black/grey background.
Dont like: To much information and pictures on the first front page.
Elegant
black background
grey backgrund
red logo
top
http://www.lindquistaro.com/
We want to have total remake on our website www.morvinkorvald.dk .
the design and setup on this brochure can be an inspiration
logo
Please place the above jpg-photos in decending order.

```html
<!DOCTYPE html>
<html lang="da">
<head>
<meta charset="utf-8">
<title>KORVALD – Projektudvikling</title>
<link rel="stylesheet" href="https://fonts.googleapis.com/css2?family=Arimo:wght@400;700&display=swap">
<style>
  :root {
    --bg: #000000;
    --brand-text: #d9d9d9;
    --brand-red: #c8102e;
    --nav-top: #8a8a8a;
    --nav-bottom: #3a3a3a;
    --nav-edge: #bcbcbc;
    --nav-active: #b01a3a;
    --text: #ffffff;
    --muted: #cfcfcf;
    --bullet-red: #d0608a;
  }
  * { box-sizing: border-box; margin: 0; padding: 0; }
  html, body { width: 1200px; height: 874px; overflow: hidden; background: var(--bg); }
  body { font-family: "Arimo", Arial, sans-serif; color: var(--text); position: relative; }

  .brand {
    position: absolute; left: 290px; top: 42px;
    display: flex; align-items: center; gap: 10px;
  }
  .brand-mark { width: 16px; height: 16px; background: var(--brand-red); }
  .brand-name { font-weight: 700; font-size: 28px; color: var(--brand-text); letter-spacing: 1px; line-height: 1; }

  .social {
    position: absolute; left: 924px; top: 98px;
    font-weight: 700; font-size: 14px; color: var(--text);
  }

  .main-nav {
    position: absolute; left: 216px; top: 144px; width: 787px; height: 72px;
    border: 2px solid var(--nav-edge); border-radius: 6px;
    background: linear-gradient(var(--nav-top), var(--nav-bottom));
    display: flex; align-items: stretch; padding: 6px 8px;
  }
  .nav-item {
    display: flex; flex-direction: column; align-items: center; justify-content: center;
    border-right: 1px solid #222; border-left: 1px solid #999;
    font-size: 9px; font-weight: 700; color: #e6e6e6; letter-spacing: 0.5px;
  }
  .nav-item.is-active { background: linear-gradient(#d04060, var(--nav-active)); }
  .nav-icon {
    width: 20px; height: 16px; border-radius: 50%;
    background: radial-gradient(circle at 40% 35%, #fff, #888 70%);
    margin-bottom: 6px;
  }
  .nav-item.is-active .nav-icon { background: radial-gradient(circle at 40% 35%, #fff, #d04060 70%); }
  .nav-search {
    margin-left: 30px; align-self: center; width: 160px; height: 22px;
    background: #f2f2f2; border-radius: 11px; display: flex; align-items: center;
    justify-content: space-between; padding: 0 8px; font-size: 8px; color: #888;
  }

  .services { position: absolute; left: 268px; top: 356px; list-style: none; }
  .services li {
    display: flex; align-items: center; height: 39px;
    font-size: 13px; font-weight: 700; color: var(--text);
  }
  .services li::before {
    content: ""; width: 14px; height: 14px; border-radius: 50%; margin-right: 12px;
    background: radial-gradient(circle at 40% 35%, #fff, #888 75%);
  }
  .services li.is-lead::before { background: radial-gradient(circle at 40% 35%, #fff, var(--bullet-red) 75%); }

  .gallery { position: absolute; left: 662px; top: 331px; width: 346px; height: 341px; }
  .tile { position: absolute; border: 2px solid #ddd; }
  .tile-a { left: 0; top: 0; width: 112px; height: 108px; background: linear-gradient(135deg, #7ea05a, #3e5a3a); }
  .tile-b { left: 117px; top: 0; width: 112px; height: 108px; background: linear-gradient(135deg, #d040a0, #601850); }
  .tile-c { left: 234px; top: 0; width: 112px; height: 108px; background: linear-gradient(135deg, #5878c8, #1a2660); }
  .tile-d { left: 0; top: 120px; width: 221px; height: 221px; background: linear-gradient(160deg, #c8b89a, #5a4a38); }
  .tile-e { left: 226px; top: 120px; width: 120px; height: 106px; background: linear-gradient(135deg, #a060d0, #3a1860); }
  .tile-f { left: 226px; top: 235px; width: 120px; height: 106px; background: linear-gradient(135deg, #70d070, #1e5a28); }

  .footer-nav {
    position: absolute; left: 0; right: 0; top: 838px;
    display: flex; justify-content: center; gap: 22px;
    font-size: 10px; color: var(--muted);
  }
</style>
</head>
<body>
  <header class="brand">
    <span class="brand-mark"></span>
    <span class="brand-name">KORVALD</span>
  </header>

  <a class="social">Linkora</a>

  <nav class="main-nav">
    <div class="nav-item" style="width:72px"><span class="nav-icon"></span>FIRMAET</div>
    <div class="nav-item is-active" style="width:136px"><span class="nav-icon"></span>PROJEKTUDVIKLING</div>
    <div class="nav-item" style="width:103px"><span class="nav-icon"></span>REFERENCER</div>
    <div class="nav-item" style="width:100px"><span class="nav-icon"></span>UDLEJNING</div>
    <div class="nav-item" style="width:80px"><span class="nav-icon"></span>PRESSE</div>
    <div class="nav-item" style="width:84px"><span class="nav-icon"></span>KONTAKT</div>
    <div class="nav-search"><span>SEARCH</span>
      <svg width="10" height="10" viewBox="0 0 10 10"><circle cx="4" cy="4" r="3" fill="none" stroke="#555" stroke-width="1.4"/><line x1="6.2" y1="6.2" x2="9.5" y2="9.5" stroke="#555" stroke-width="1.6"/></svg>
    </div>
  </nav>

  <ul class="services">
    <li class="is-lead">Developing real estate company in Denmark.</li>
    <li>Consulting Competence</li>
    <li>Handling of a project:</li>
    <li>Analysis of local conditions and market analysis</li>
    <li>Functional and usability concept</li>
    <li>Analysis of profitability</li>
    <li>Financing and utilization strategies</li>
    <li>Economic and Technical project control</li>
  </ul>

  <section class="gallery">
    <div class="tile tile-a" role="img" aria-label="Green-tinted photo of a modern commercial building"></div>
    <div class="tile tile-b" role="img" aria-label="Magenta-tinted photo of a retail building facade"></div>
    <div class="tile tile-c" role="img" aria-label="Blue-tinted photo of a store front"></div>
    <div class="tile tile-d" role="img" aria-label="Sepia photo of a courtyard with a tree and benches"></div>
    <div class="tile tile-e" role="img" aria-label="Purple-tinted photo of a building entrance"></div>
    <div class="tile tile-f" role="img" aria-label="Green-tinted photo of a shop building"></div>
  </section>

  <footer class="footer-nav">
    <span>Home</span><span>About Us</span><span>Portfolio</span><span>News</span><span>Services</span><span>Contact</span>
  </footer>
</body>
</html>
```